Need a stunning looking Business Card Design for my Telecom Business, Wow FACTOR!

I deal with high level IT Directors , and Contractors.
I need to impress them with a sleek , professional and unique business card.
Im thinking options as far as rounded edges, plastic , or even metal card or die cut on a corner.
Whatever looks better and leave an unforgettable first impression.
im looking for the wow factor.
Front should have the basics info (attached on the picture of current business card)
i would like to add picture of myself somewhere
Back side
should have logo and maybe some pictures or past projects, you can download from my website ( www.lumvexholdings.com)

```html
<!DOCTYPE html>
<html lang="en">
<head>
<meta charset="utf-8">
<title>Lumvex Networks – Business Card</title>
<link rel="stylesheet" href="https://fonts.googleapis.com/css2?family=Open+Sans:wght@400;600;700&display=swap">
<style>
  :root {
    --backdrop: #a9a9a9;
    --navy-deep: #0d2550;
    --navy-mid: #1f3f6e;
    --steel: #4c6a93;
    --white: #ffffff;
    --cable-yellow: #f2c52a;
    --cable-pink: #e8327a;
    --cable-red: #d9253a;
    --cable-teal: #19b59a;
    --cable-blue: #2a62c9;
    --shirt-grey: #8f8d93;
  }
  * { margin: 0; padding: 0; box-sizing: border-box; }
  html, body {
    width: 1200px;
    height: 1000px;
    overflow: hidden;
    background: var(--backdrop);
    font-family: "Open Sans", Arial, sans-serif;
  }
  .canvas { position: relative; width: 1200px; height: 1000px; }

  .card {
    position: absolute;
    left: 294px;
    width: 613px;
    height: 351px;
    border-radius: 22px;
    overflow: hidden;
    color: var(--white);
  }

  /* Brand side */
  .card--brand { top: 93px; }
  .brand-photo {
    position: absolute; inset: 0;
    background:
      radial-gradient(ellipse at 20% 80%, var(--cable-yellow) 0%, transparent 45%),
      radial-gradient(ellipse at 40% 20%, var(--cable-pink) 0%, transparent 45%),
      radial-gradient(ellipse at 75% 75%, var(--cable-red) 0%, transparent 45%),
      radial-gradient(ellipse at 85% 15%, var(--cable-teal) 0%, transparent 45%),
      linear-gradient(120deg, #f6d24a 0%, #ef6a8c 40%, #c8334f 65%, #1f8fb0 85%, #17b492 100%);
  }
  .brand-wordmark {
    position: absolute;
    left: 0; right: 0; top: 150px;
    display: flex; align-items: center; justify-content: center; gap: 14px;
    font-weight: 600;
    font-size: 40px;
    letter-spacing: 3px;
  }
  .brand-wordmark .mark-square {
    width: 26px; height: 26px; background: var(--white);
  }

  /* Contact side */
  .card--contact { top: 547px; }
  .site-photo {
    position: absolute; inset: 0;
    background: linear-gradient(180deg, var(--steel) 0%, var(--navy-mid) 45%, var(--navy-deep) 100%);
  }
  .portrait {
    position: absolute;
    left: 354px; top: 0;
    width: 259px; height: 351px;
    background: linear-gradient(180deg, rgba(76,106,147,0) 0%, #6f7480 45%, var(--shirt-grey) 100%);
  }
  .contact-wordmark {
    position: absolute;
    left: 41px; top: 52px;
    display: flex; align-items: center; gap: 10px;
    font-weight: 600;
    font-size: 22px;
    letter-spacing: 2px;
  }
  .contact-wordmark .mark-square { width: 16px; height: 16px; background: var(--white); }

  .person-name {
    position: absolute; left: 41px; top: 138px;
    font-weight: 700; font-size: 38px; line-height: 1;
  }
  .person-role {
    position: absolute; left: 41px; top: 190px;
    font-weight: 400; font-size: 21px;
  }
  .contact-list {
    position: absolute; left: 44px; top: 236px;
    list-style: none;
  }
  .contact-list li {
    display: flex; align-items: center; gap: 14px;
    height: 32px;
    font-size: 18px;
  }
  .contact-list svg {
    width: 22px; height: 22px;
    fill: none; stroke: var(--white); stroke-width: 1.4;
    stroke-linecap: round; stroke-linejoin: round;
  }
</style>
</head>
<body>
<div class="canvas">

  <section class="card card--brand">
    <div class="brand-photo" role="img" aria-label="Close-up photo of colourful network cable connectors"></div>
    <div class="brand-wordmark"><span class="mark-square"></span>LUMVEX NETWORKS</div>
  </section>

  <section class="card card--contact">
    <div class="site-photo" role="img" aria-label="Photo of a warehouse steel roof structure in navy tones"></div>
    <div class="portrait" role="img" aria-label="Portrait photo of the operations manager in a grey company shirt"></div>

    <div class="contact-wordmark"><span class="mark-square"></span>LUMVEX NETWORKS</div>
    <h1 class="person-name">Daniel Okafor</h1>
    <p class="person-role">Operations Manager</p>

    <ul class="contact-list">
      <li>
        <svg viewBox="0 0 24 24"><path d="M5 3h4l2 5-2.5 1.5a11 11 0 0 0 6 6L16 13l5 2v4a2 2 0 0 1-2 2A16 16 0 0 1 3 5a2 2 0 0 1 2-2z"/></svg>
        <span>(954) 555-0172</span>
      </li>
      <li>
        <svg viewBox="0 0 24 24"><rect x="2" y="5" width="20" height="14"/><path d="M2 5l10 8 10-8M2 19l7-7M22 19l-7-7"/></svg>
        <span>info@lumvexholdings.com</span>
      </li>
      <li>
        <svg viewBox="0 0 24 24"><circle cx="12" cy="12" r="9.5"/><path d="M2.5 12h19M12 2.5c3 3 3 16 0 19M12 2.5c-3 3-3 16 0 19M4 7h16M4 17h16"/></svg>
        <span>lumvexholdings.com</span>
      </li>
    </ul>
  </section>

</div>
</body>
</html>
```